IT support company needs Banner Ad for the top of their quote layout template

We need a banner Ad for the top of our for quote layout template so it is sent out on all our quotes

The banner size must be 827 x 100 pixels - anything larger than 60 KB can cause upload time issues

We have attached our logo and examples of the quote page to see how it looks in the context of the whole page.

Essential elements of the banner
- Must have our logo but this can be changed to be different colours if it makes the design work better i.e. Tidal Ember could be all in white

Colours
- Can use all of our standard colours - Orange, Black, Grey and White

Images
- As a premium IT support company we deal with people and technology so would like to see both of these Incorporated into the banner i.e. people using technology These images could be watermarked or one colour effect.

Look and Feel
- Professional, friendly, people, technology, premium

Target Market
Small business owners and managers

Industry/Entity Type

It Company

```html
<!DOCTYPE html>
<html lang="nl">
<head>
<meta charset="utf-8">
<title>Offerte LM-000280</title>
<link rel="stylesheet" href="https://fonts.googleapis.com/css2?family=Carlito:wght@400;700&display=swap">
<style>
:root{
  --ink:#111;
  --blue:#1a78c2;
  --rule:#1b75c4;
  --orange:#f26a1b;
  --steel:#8a8f94;
  --stripe:#f3f3f3;
  --head-a:#cfe6f8;
  --head-b:#eaf4fc;
}
*{box-sizing:border-box;margin:0;padding:0}
html,body{width:888px;height:1200px;overflow:hidden;background:#fff}
body{font-family:"Carlito",Calibri,Arial,sans-serif;color:var(--ink)}
.page{position:absolute;left:0;top:0;width:827px;height:1118px;transform:scale(1.0738);transform-origin:0 0}
.abs{position:absolute}

/* banner */
.banner{left:0;top:0;width:827px;height:100px;background:#fff}
.banner-people{left:0;top:0;width:282px;height:100px;background:linear-gradient(180deg,#6d7378,#b9bcbf 60%,#9a9ea2)}
.banner-tech{left:580px;top:0;width:247px;height:100px;background:linear-gradient(135deg,#5a2a16,#c0623a 45%,#e7a17d 75%,#8c3b1c)}
.banner-bar{top:0;width:8px;height:100px;background:var(--orange)}
.brand{left:290px;top:0;width:280px;height:100px;display:flex;align-items:center;justify-content:center;gap:8px;font-weight:700;font-size:30px;letter-spacing:.5px;color:#1b1b1b}
.brand-dot{width:12px;height:12px;border-radius:50%;background:var(--orange)}
.banner-rule{left:0;top:103px;width:827px;height:5px;background:linear-gradient(90deg,#1b75c4,#4ab3ea)}

h1{position:absolute;left:26px;top:140px;font-size:21px;font-weight:400}
.portrait{left:26px;top:180px;width:98px;height:130px;background:linear-gradient(180deg,#c9c9c9,#8d8d8d)}
.info{position:absolute;top:178px;font-size:13px;line-height:17px}
.info h3{color:var(--blue);font-weight:400;font-size:16px;margin-bottom:6px}
.info b{font-weight:700}
.sep{left:26px;top:322px;width:775px;height:3px;background:var(--rule)}

h2{position:absolute;left:26px;font-size:18px;font-weight:400}
.tbl{position:absolute;left:26px;width:775px;border:1px solid var(--ink);border-collapse:collapse;font-size:13px}
.tbl th{height:25px;font-weight:400;text-align:left;padding:0 5px;background:linear-gradient(90deg,var(--head-a),var(--head-b) 50%,var(--head-a))}
.tbl td{height:26px;padding:0 5px}
.tbl tr:nth-child(even) td{background:var(--stripe)}
.tbl .num{text-align:right}
.tbl .col{border-left:1px solid var(--ink)}
.sum{position:absolute;right:32px;display:flex;font-size:13px}
.sum span{color:var(--blue);text-align:right}
.sum b{width:107px;text-align:right}
.note{left:26px;top:925px;font-size:13px}
.sign{top:996px;height:1px;background:var(--ink)}
.sign-label{top:999px;font-size:13px}
.foot-line{left:0;top:1072px;width:827px;height:4px;background:var(--rule)}
.foot{left:0;top:1078px;width:827px;height:40px;background:linear-gradient(90deg,#e3f2fc,#5fbdee 50%,#e3f2fc);display:flex;justify-content:space-between;align-items:center;padding:0 27px;font-size:13px}
</style>
</head>
<body>
<div class="page">
  <header class="abs banner">
    <div class="abs banner-people" role="img" aria-label="Businesspeople pushing large gears, greyscale photo"></div>
    <div class="abs banner-bar" style="left:282px"></div>
    <div class="abs brand"><span class="brand-dot"></span>TIDAL EMBER</div>
    <div class="abs banner-bar" style="left:572px"></div>
    <div class="abs banner-tech" role="img" aria-label="Hands typing on a keyboard, orange-toned photo"></div>
  </header>
  <div class="abs banner-rule"></div>

  <h1>Standard MSP&nbsp; #2</h1>
  <div class="abs portrait" role="img" aria-label="Portrait photo of the sender"></div>
  <div class="info" style="left:135px">
    <h3>Opgesteld door:</h3>
    <b>Lena Marsh Inc</b><br>Lena Marsh<br><br>Fax<br>lena.marsh@quotewell.com
  </div>
  <div class="info" style="left:360px">
    <h3>Opgesteld voor:</h3>
    <b>Copper Ridge</b><br>1820 Harlow Ave.<br>Fairview,&nbsp;&nbsp; 48210<br>Nora Ellis<br>tom.vance@bluefinch.co.uk
  </div>
  <div class="info" style="left:627px">
    <h3>Gegevens Offerte:</h3>
    <b>Offerte #: LM-000280</b><br>Versie: 1<br>Leverdatum: 14/11/2017<br>Vervaldatum: 31/12/2017
  </div>
  <div class="abs sep"></div>

  <h2 style="top:341px">Overzicht Offerte</h2>
  <table class="tbl" style="top:370px">
    <tr><th>Beschrijving</th><th class="num col" style="width:109px">Bedrag</th></tr>
    <tr><td style="background:#fff">Initial Investment</td><td class="num col" style="background:#fff">$800.00</td></tr>
  </table>
  <div class="sum" style="top:429px"><span>Subtotaal:</span><b>$800.00</b></div>
  <div class="sum" style="top:454px"><span>VAT:</span><b>$160.00</b></div>
  <div class="sum" style="top:480px"><span>Totaal:</span><b>$960.00</b></div>

  <h2 style="top:517px">Overzicht Terugkerende Kosten</h2>
  <table class="tbl" style="top:546px">
    <tr><th>Beschrijving</th><th class="num col" style="width:109px">Bedrag</th></tr>
    <tr><td>Monitoring</td><td class="num col">$375.00</td></tr>
    <tr><td>Support</td><td class="num col">$65.00</td></tr>
    <tr><td>Fixed Hours</td><td class="num col">$850.00</td></tr>
  </table>
  <div class="sum" style="top:657px"><span>Terugkerende totaal:</span><b>$1,290.00</b></div>

  <h2 style="top:696px">*Optionele kosten</h2>
  <table class="tbl" style="top:723px">
    <tr><th>Beschrijving</th><th class="num col" style="width:108px">Recurring</th><th class="num col" style="width:109px">One-Time</th></tr>
    <tr><td>Monitoring</td><td class="num col">$790.00</td><td class="num col">$0.00</td></tr>
    <tr><td>Support</td><td class="num col">$185.00</td><td class="num col">$0.00</td></tr>
    <tr><td>Fixed Hours</td><td class="num col">$695.00</td><td class="num col">$0.00</td></tr>
    <tr><td>Add-on Services</td><td class="num col">$850.00</td><td class="num col">$0.00</td></tr>
  </table>
  <div class="sum" style="top:862px"><span>Optionele terugkerend bedrag:</span><b>$2,520.00</b></div>
  <div class="sum" style="top:886px"><span>Optionele ongeplande Subtotaal:</span><b>$.00</b></div>

  <p class="abs note">Taxes, shipping, handling and other fees may apply.&nbsp; We reserve the right to cancel orders arising from pricing or other errors.</p>

  <div class="abs sign" style="left:26px;width:463px"></div>
  <div class="abs sign-label" style="left:26px">Handtekening</div>
  <div class="abs sign" style="left:519px;width:182px"></div>
  <div class="abs sign-label" style="left:521px">Datum</div>

  <div class="abs foot-line"></div>
  <footer class="abs foot"><span>Offerte #LM-000280 v1</span><span>Pagina 6 Van 7</span></footer>
</div>
</body>
</html>
```